Luxury Black and Gold Business Card Design for Jewelry website

We would like the following:
* Two-sided card (front and back side need to be black with gold logo and text)
* Simple design
* Size 9х5cm

Front side Information:
- Logo (The logo and all text need to be Gold and all business card need to be black baground)
- Icon for Website and address: www.ZlatenPrusten.com (use fancy font and gold color and icon)
- Instagram Icon and addres: ZlatenPrusten (use fancy font and gold color and icon)
- Facebook Icon and address: ZlatenPrusten (use fancy font and gold color and icon)

Back Side information:
"Никога не подценявай себе си.
Всичко, което останалите правят,
можеш да го направиш и ти."
www.ZlatenPrusten.com

```html
<!DOCTYPE html>
<html lang="bg">
<head>
<meta charset="utf-8">
<title>Златено – визитка</title>
<link rel="stylesheet" href="https://fonts.googleapis.com/css2?family=Open+Sans:wght@400;700&display=swap">
<style>
  :root {
    --stage: #2b2b2b;
    --card: #0b0b0b;
    --card-edge: #1a1a1a;
    --gold: #e6b422;
  }
  html, body {
    margin: 0;
    padding: 0;
    width: 1200px;
    height: 780px;
    overflow: hidden;
    background: var(--stage);
    font-family: "Open Sans", Arial, sans-serif;
  }
  .stage {
    position: relative;
    width: 1200px;
    height: 780px;
  }
  .card {
    position: absolute;
    width: 540px;
    height: 300px;
    background: radial-gradient(ellipse at 50% 40%, var(--card-edge), var(--card) 75%);
    box-shadow: 0 6px 18px rgba(0,0,0,.45);
    color: var(--gold);
    box-sizing: border-box;
  }
  .card--front { left: 90px; top: 70px; }
  .card--back  { left: 570px; top: 410px; }

  .brand {
    display: flex;
    flex-direction: column;
    align-items: center;
  }
  .brand__name {
    font-weight: 700;
    font-size: 52px;
    letter-spacing: 2px;
    line-height: 1;
    color: var(--gold);
  }
  .brand__tagline {
    font-size: 11px;
    letter-spacing: 1.5px;
    margin-top: 6px;
    text-transform: uppercase;
  }
  .card--front .brand {
    position: absolute;
    left: 0; right: 0; top: 86px;
  }
  .contacts {
    position: absolute;
    left: 28px; right: 28px; bottom: 34px;
    display: flex;
    justify-content: space-between;
    align-items: center;
    font-weight: 700;
    font-size: 14px;
  }
  .contacts__item {
    display: flex;
    align-items: center;
    gap: 6px;
  }
  .contacts__mark {
    width: 13px;
    height: 13px;
    background: var(--gold);
    border-radius: 3px;
  }

  .card--back .brand {
    position: absolute;
    left: 60px; top: 34px;
    align-items: flex-start;
  }
  .card--back .brand__name { font-size: 44px; }
  .quote {
    position: absolute;
    left: 60px; top: 136px;
    margin: 0;
    font-size: 17px;
    line-height: 1.45;
  }
  .back-web {
    position: absolute;
    left: 60px; right: 30px; top: 228px;
    display: flex;
    align-items: center;
    gap: 10px;
    font-size: 14px;
  }
  .back-web__rule {
    flex: 1;
    height: 2px;
    background: var(--gold);
  }
  .back-rule {
    position: absolute;
    left: 30px; right: 30px; bottom: 24px;
    height: 2px;
    background: var(--gold);
  }
</style>
</head>
<body>
<main class="stage">
  <section class="card card--front" aria-label="Лице на визитката">
    <div class="brand">
      <span class="brand__name">ZLATENO</span>
      <span class="brand__tagline">стил и класа за всеки ден</span>
    </div>
    <div class="contacts">
      <span class="contacts__item">www.ZlatenPrusten.com</span>
      <span class="contacts__item"><span class="contacts__mark"></span>ZlatenPrusten</span>
      <span class="contacts__item"><span class="contacts__mark"></span>ZlatenPrusten</span>
    </div>
  </section>

  <section class="card card--back" aria-label="Гръб на визитката">
    <div class="brand">
      <span class="brand__name">ZLATENO</span>
      <span class="brand__tagline">стил и класа за всеки ден</span>
    </div>
    <p class="quote">Никога не подценявай себе си.<br>Всичко, което останалите правят,<br>можеш да го направиш и ти.</p>
    <div class="back-web">
      <span>www.ZlatenPrusten.com</span>
      <span class="back-web__rule"></span>
    </div>
    <div class="back-rule"></div>
  </section>
</main>
</body>
</html>
```